Valduro.com needs a Mobile FIRST Site

Valduro.com is an insurance broker based in Panama City, Panama that plans to sell car and motorcycle insurance online.

We need to design a total of 5 pages (two of those are A/B test pages). The site will be responsive and will be programmed in React. We will be using Brisk Widget´s library to code Valduro.com. Keep in mind that we are using Brisk Widget to program the site´s functions, not to create the "look and feel" of the site, that is obviously your job. You can learn more about Brisk Widget here... https://brisk-widget.example/

We have created wireframes for the app. Please follow and keep in mind the instructions in the wireframes. You can change things here and there as long as the core functions and goals stay intact. We have uploaded the wireframes along with the company logo and color.

We are planning to A/B test the site´s home page so we need to design two homepages. You can find homepage A and B in the wireframes provided.

We speak Spanish in Panama but you can design the site in English. We can change the text once we receive the designs.

Target Market(s)

25-45 year olds who own a car or motorcylcle and own a credit card.

Industry/Entity Type

Insurance

Font styles to use
Sans Serif

Requirements
Must have
• Follow the wireframes provided and the logo colors.
Nice to have
• Please look at the Image I´ve uploaded from DeskHaven, use it as reference to create HomePage A.

```html
<!DOCTYPE html>
<html lang="en">
<head>
<meta charset="utf-8">
<title>Valduro.com – Mobile Home</title>
<link href="https://fonts.googleapis.com/css2?family=Varela+Round&family=Montserrat:wght@600;700&display=swap" rel="stylesheet">
<style>
  :root {
    --purple: #47298a;
    --purple-dark: #3b2177;
    --page-bg: #eeeeee;
    --screen-bg: #ececec;
    --white: #ffffff;
    --ink: #2b2b2b;
    --track: #eeeeee;
    --photo-dark: #1e1e1e;
    --photo-red: #8f1219;
  }
  * { box-sizing: border-box; margin: 0; padding: 0; }
  html, body { width: 1200px; height: 900px; overflow: hidden; background: var(--page-bg); }
  body { font-family: "Varela Round", "Helvetica Neue", Arial, sans-serif; color: var(--ink); position: relative; }

  .screen {
    position: absolute; left: 353px; top: 15px;
    width: 412px; height: 724px;
    transform: scale(1.2); transform-origin: top left;
    background: var(--screen-bg); overflow: hidden;
  }

  .status-bar {
    height: 26px; background: var(--purple); color: var(--white);
    font-family: Arial, Helvetica, sans-serif; font-size: 12px;
    display: flex; align-items: center; justify-content: space-between; padding: 0 8px;
  }
  .status-left { display: flex; align-items: center; gap: 5px; }
  .signal { letter-spacing: -1px; font-size: 10px; }
  .status-right { display: flex; align-items: center; gap: 4px; }
  .battery { width: 24px; height: 10px; border: 1px solid var(--white); border-radius: 2px; padding: 1px; }
  .battery span { display: block; width: 100%; height: 100%; background: var(--white); border-radius: 1px; }

  .app-header {
    height: 50px; background: var(--purple); color: var(--white);
    display: flex; align-items: center; justify-content: space-between; padding: 0 12px;
  }
  .brand-name { font-family: "Montserrat", sans-serif; font-weight: 700; font-size: 19px; letter-spacing: -0.3px; }
  .cart { position: relative; width: 24px; height: 24px; }
  .cart-badge {
    position: absolute; top: -2px; right: -3px; width: 11px; height: 11px; border-radius: 50%;
    background: #6a4bc4; color: var(--white); font-size: 8px; line-height: 11px; text-align: center;
  }

  .intro { text-align: center; padding-top: 16px; }
  .intro-title { color: var(--purple); font-size: 24px; font-weight: 400; letter-spacing: 0.3px; }
  .intro-sub { font-size: 14px; line-height: 16px; margin-top: 5px; letter-spacing: 0.3px; }

  .steps { display: flex; align-items: center; justify-content: center; margin-top: 17px; font-size: 15px; }
  .step { display: flex; align-items: center; gap: 12px; }
  .step-done { color: var(--purple); }
  .step-num {
    width: 24px; height: 24px; border: 1.5px solid var(--ink); border-radius: 50%;
    font-size: 13px; line-height: 21px; text-align: center;
  }
  .step-line { width: 50px; height: 1.5px; background: var(--purple); margin: 0 7px; }

  .vehicle-toggle {
    margin: 21px auto 0; width: 332px; height: 40px; background: var(--white);
    border-radius: 20px; display: flex; align-items: center;
  }
  .toggle-option {
    height: 40px; border-radius: 20px; display: flex; align-items: center; justify-content: center; gap: 12px;
    font-family: "Montserrat", sans-serif; font-weight: 700; font-size: 16px; color: var(--purple);
  }
  .toggle-active { width: 138px; background: var(--purple); color: var(--white); }
  .toggle-option:last-child { flex: 1; }

  .plan-photo {
    position: relative; height: 188px; margin-top: 23px;
    background: radial-gradient(ellipse 70% 55% at 55% 60%, var(--photo-red) 0%, #5a1015 45%, transparent 75%),
                linear-gradient(180deg, #1b1b1b 0%, #3b3b3b 65%, #9a9a9a 100%);
    box-shadow: 0 1px 4px rgba(0,0,0,0.3);
  }
  .plan-photo.next { height: 60px; margin-top: 3px;
    background: radial-gradient(ellipse 60% 60% at 45% 100%, #5a1015 0%, transparent 70%),
                linear-gradient(180deg, #161616 0%, #2c2c2c 100%); }
  .plan-name {
    position: absolute; right: 19px; top: 15px; color: var(--white);
    font-family: "Montserrat", sans-serif; font-weight: 700; font-size: 17px; letter-spacing: 0.2px;
  }
  .plan-price { position: absolute; left: 20px; bottom: 20px; color: var(--white); font-size: 21px; }
  .buy-button {
    position: absolute; right: 20px; bottom: 10px; width: 116px; height: 46px; border-radius: 23px;
    background: var(--purple); color: var(--white); text-align: center; line-height: 46px;
    font-family: "Montserrat", sans-serif; font-weight: 700; font-size: 14px; letter-spacing: 0.2px;
  }

  .plan-details { background: var(--white); padding: 24px 20px 16px; }
  .coverage-row { display: flex; align-items: center; height: 24px; margin-bottom: 13.5px; }
  .coverage-label { width: 189px; font-size: 14px; letter-spacing: 0.2px; }
  .coverage-track { flex: 1; height: 24px; border-radius: 12px; background: var(--track); }
  .coverage-fill {
    height: 24px; border-radius: 12px; background: var(--purple); color: var(--white);
    font-family: Arial, sans-serif; font-size: 12px; line-height: 24px; padding-left: 12px;
  }
  .trust-list { display: flex; justify-content: space-between; margin-top: 14px; }
  .trust-item { display: flex; align-items: center; gap: 7px; font-size: 11.5px; line-height: 14px; }
</style>
</head>
<body>
<main class="screen">
  <div class="status-bar">
    <div class="status-left"><span class="signal">●●●●●</span>
      <svg width="12" height="9" viewBox="0 0 12 9"><path d="M1 3.2a7 7 0 0 1 10 0M2.8 5a4.5 4.5 0 0 1 6.4 0" stroke="#fff" stroke-width="1.3" fill="none"/><circle cx="6" cy="7.3" r="1.2" fill="#fff"/></svg>
      <span>Nolvo Tel</span></div>
    <span>9:41 AM</span>
    <div class="status-right"><span>100%</span><div class="battery"><span></span></div></div>
  </div>

  <header class="app-header">
    <svg width="22" height="16" viewBox="0 0 22 16"><path d="M0 1h22M0 8h22M0 15h22" stroke="#fff" stroke-width="1.8"/></svg>
    <span class="brand-name">Valduro.com</span>
    <div class="cart">
      <svg width="22" height="22" viewBox="0 0 22 22"><path d="M2 6h3l2.5 9h9l2-7H6" stroke="#fff" stroke-width="1.6" fill="none" stroke-linejoin="round"/><circle cx="9" cy="18" r="1.4" fill="#fff"/><circle cx="15" cy="18" r="1.4" fill="#fff"/></svg>
      <span class="cart-badge">2</span>
    </div>
  </header>

  <section class="intro">
    <h1 class="intro-title">The Claim Aquí</h1>
    <p class="intro-sub">compare and claim car insurance<br>in easy way</p>
  </section>

  <nav class="steps">
    <div class="step step-done">
      <svg width="25" height="25" viewBox="0 0 25 25"><circle cx="12.5" cy="12.5" r="12.5" fill="#47298a"/><path d="M7 12.5l4 4 7-8" stroke="#fff" stroke-width="2" fill="none"/></svg>
      <span>Elige</span></div>
    <div class="step-line"></div>
    <div class="step"><span class="step-num">2</span><span>Datos</span></div>
    <div class="step-line"></div>
    <div class="step"><span class="step-num">3</span><span>Paga</span></div>
  </nav>

  <div class="vehicle-toggle">
    <div class="toggle-option toggle-active">
      <svg width="40" height="16" viewBox="0 0 40 16"><path d="M2 11v-3l6-1 5-5h13l6 5 6 1v3z" fill="#fff"/><circle cx="10" cy="12" r="3.2" fill="#47298a" stroke="#fff" stroke-width="1.5"/><circle cx="31" cy="12" r="3.2" fill="#47298a" stroke="#fff" stroke-width="1.5"/></svg>
      <span>Car</span></div>
    <div class="toggle-option">
      <svg width="38" height="20" viewBox="0 0 38 20"><circle cx="8" cy="13" r="6" fill="none" stroke="#47298a" stroke-width="2"/><circle cx="30" cy="13" r="6" fill="none" stroke="#47298a" stroke-width="2"/><path d="M8 13l7-7h9l6 7M14 6l8 7h4" fill="none" stroke="#47298a" stroke-width="2.5"/></svg>
      <span>Motorcycle</span></div>
  </div>

  <article class="plan">
    <div class="plan-photo" role="img" aria-label="Photo of a red sports car on a dark studio background">
      <span class="plan-name">Name of Insurance</span>
      <span class="plan-price">$10,000</span>
      <span class="buy-button">BUY NOW</span>
    </div>
    <div class="plan-details">
      <div class="coverage-row"><span class="coverage-label">insurance coverage</span><div class="coverage-track"><div class="coverage-fill" style="width:129px">$7,000</div></div></div>
      <div class="coverage-row"><span class="coverage-label">accident coverage</span><div class="coverage-track"><div class="coverage-fill" style="width:104px">$5,000</div></div></div>
      <div class="coverage-row"><span class="coverage-label">other coverage</span><div class="coverage-track"><div class="coverage-fill" style="width:92px">$4,000</div></div></div>
      <div class="trust-list">
        <div class="trust-item">
          <svg width="33" height="33" viewBox="0 0 33 33"><path d="M16.5 1l4 3.5 5-.5 1.5 5 4.5 2.5-2 4.5 2 4.5-4.5 2.5-1.5 5-5-.5-4 3.5-4-3.5-5 .5-1.5-5L1.5 21l2-4.5-2-4.5L6 9.5 7.5 4.5l5 .5z" fill="#47298a"/><path d="M11 16.5l4 4 7-8" stroke="#fff" stroke-width="2" fill="none"/></svg>
          <span>trusted<br>insurance</span></div>
        <div class="trust-item">
          <svg width="31" height="31" viewBox="0 0 31 31"><circle cx="15.5" cy="15.5" r="14" fill="none" stroke="#47298a" stroke-width="2.2"/><text x="15.5" y="20.5" text-anchor="middle" font-family="Arial" font-weight="700" font-size="14" fill="#47298a">($)</text></svg>
          <span>money back<br>guarantee</span></div>
        <div class="trust-item">
          <svg width="28" height="32" viewBox="0 0 28 32"><path d="M14 1L2 5v9c0 8 5 14 12 17 7-3 12-9 12-17V5z" fill="#47298a"/><path d="M14 5v12H5.5V7.5z" fill="#fff"/><path d="M14 17h8.5c-.8 5-4 8.5-8.5 10.5z" fill="#fff"/></svg>
          <span>full<br>protection</span></div>
      </div>
    </div>
  </article>

  <article class="plan">
    <div class="plan-photo next" role="img" aria-label="Photo of a red sports car for the next insurance plan">
      <span class="plan-name">Name of Insurance</span>
    </div>
  </article>
</main>
</body>
</html>
```